self-employed education content specialist/consultant needs business card and logo design

I need a design for a double-sided business card (and logo) for my nascent consultancy business based in London UK, to hand out at a London trade show in a couple of weeks. The business simply has my name, "Marcus Tenwold".

I describe my service as a "content and engagement consultant". In essence I cover 2 areas:
- Advice to organisations on effective strategies and tactics for creating and distributing large volumes of media-rich content (video and interactive) for learning, training and professional development, that successfully engages and impacts on students and their teachers.
- Advice on growing and maintaining customer/end-user engagement to help maximise the reach and usage of this content.

I have uploaded a weighted list of key words that offer I hope a good feel of "the brand".

In terms of design I have put together a very rough initial idea for the card (see attached doc), which gives an idea of the key messages in text, but I feel it is not working visually, and looks too amateur. In particular I think the background/visuals of the info side needs work; the word cloud on the back of the card is perhaps rather "passé" and could be improved on; there is no "logo" at present; and I think overall it's not very "creative", i.e. it doesn't "stand out".

I am not set on font or background colours/design. The font itself should not be too businessy or too "comic sans", hence I've currently gone for something like Odile or Playfair Display.

Also note that
1. given budget and time constraints, I'm looking for designs for printing on paper, and to be of a fairly standard business card shape/size.
2. I have no web address at present, but will need a card design that can cope with this being added at a later date.

Overall I am hoping for something fairly clean, simple and clear, that will impress and speak to senior managers/business owners working in the education and edtech sectors.

As a self-employed consultant my budget is limited, so I don't expect the world for what I can offer, but am hoping that there are design experts out there who can swiftly interpret my brief and produce something suitable for my needs.

Target Market(s)

senior managers/business owners working in the education and edtech sectors.

Contact Information for Business Card

marcus tenwold
content and engagement consultant
education - training - development
+44 (0) 7731 482905
marcus.tenwold@quorvane.com

Font styles to use
Other font styles liked:
• Odile or Playfair Display are my favourites for now.

Colors

Designer to choose colors to be used in the design.

```html
<!DOCTYPE html>
<html lang="en">
<head>
<meta charset="utf-8">
<title>Marcus Tenwold — Business Card</title>
<link rel="stylesheet" href="https://fonts.googleapis.com/css2?family=Noticia+Text:wght@400;700&display=swap">
<style>
  :root {
    --backdrop: #d9d9d9;
    --card: #ffffff;
    --band: #8f8f8f;
    --ink: #5e5e5e;
    --accent: #ee5a2b;
    --keyword: #b4b4b4;
  }
  * { margin: 0; padding: 0; box-sizing: border-box; }
  html, body {
    width: 1200px;
    height: 566px;
    overflow: hidden;
    background: var(--backdrop);
    font-family: "Noticia Text", Georgia, serif;
  }
  .stage { position: relative; width: 1200px; height: 566px; }

  .card {
    position: absolute;
    top: 148px;
    width: 497px;
    height: 276px;
    background: var(--card);
    overflow: hidden;
  }
  .card--front { left: 33px; }
  .card--back { left: 644px; }

  /* Front */
  .front__band {
    position: absolute; left: 0; top: 0;
    width: 21px; height: 100%;
    background: var(--band);
  }
  .front__role {
    position: absolute; left: 42px; top: 23px;
    font-size: 12px; letter-spacing: 0.7px;
    color: var(--ink);
    text-transform: uppercase;
  }
  .front__name {
    position: absolute; left: 42px; top: 114px;
    font-size: 23px; line-height: 27px;
    letter-spacing: 4.5px;
    color: var(--accent);
    text-transform: uppercase;
    font-weight: 700;
  }
  .front__contact {
    position: absolute; left: 42px; top: 175px;
    font-size: 15px; line-height: 25px;
    color: var(--ink);
    font-style: normal;
  }
  .front__phone { letter-spacing: 1.2px; font-size: 15.5px; }
  .front__services {
    position: absolute; left: 21px; right: 0; top: 262px;
    text-align: center;
    font-size: 9px; letter-spacing: 0.7px;
    color: var(--ink);
    text-transform: uppercase;
  }
  .front__services .dot {
    display: inline-block;
    width: 5px; height: 5px;
    border-radius: 50%;
    background: var(--accent);
    margin: 0 4px 1px 4px;
    vertical-align: middle;
  }

  /* Back */
  .keywords {
    position: absolute; left: 24px; right: 24px;
    text-align: center;
    font-size: 12.5px; line-height: 17.5px;
    color: var(--keyword);
    list-style: none;
  }
  .keywords--top { top: 12px; }
  .keywords--bottom { top: 196px; }
  .keywords li { display: inline; margin: 0 5px; }

  .wordmark {
    position: absolute; left: 0; right: 0; top: 122px;
    display: flex; align-items: center; justify-content: center;
    gap: 12px;
  }
  .wordmark__square {
    width: 14px; height: 14px;
    background: var(--accent);
  }
  .wordmark__name {
    color: var(--accent);
    font-size: 26px;
    font-weight: 700;
    white-space: nowrap;
  }
</style>
</head>
<body>
<main class="stage">

  <section class="card card--front" aria-label="Card front">
    <div class="front__band"></div>
    <p class="front__role">Content and engagement consultant</p>
    <h1 class="front__name">Marcus<br>Tenwold</h1>
    <address class="front__contact">
      marcus.tenwold@quorvane.com<br>
      <span class="front__phone">+44 (0) 7731 482905</span>
    </address>
    <p class="front__services">Education<span class="dot"></span>Training<span class="dot"></span>Development</p>
  </section>

  <section class="card card--back" aria-label="Card back">
    <ul class="keywords keywords--top">
      <li>strategy</li><li>media-rich</li><li>reach</li><li>usage</li><li>edtech</li><li>tactics</li>
      <li>organisations</li><li>teaching</li><li>growth</li><li>end-users</li><li>volume</li>
      <li>learners</li><li>curriculum</li><li>insight</li>
    </ul>

    <div class="wordmark">
      <span class="wordmark__square"></span>
      <span class="wordmark__name">Marcus Tenwold</span>
    </div>

    <ul class="keywords keywords--bottom">
      <li>retention</li><li>platforms</li><li>advice</li><li>outreach</li><li>quality</li>
      <li>resources</li><li>customers</li><li>planning</li><li>evaluation</li>
      <li>courses</li><li>formats</li><li>delivery</li><li>sector</li><li>audiences</li>
      <li>London</li>
    </ul>
  </section>

</main>
</body>
</html>
```